Fundraising Flyer for a School Library

We are a small but fast-growing school in need of funding support for a new Library, Admin and 2 more primary classrooms.
We are hoping that someone can come up with a design for a flyer (A4 - 3 fold) or brochure (2 to an A4) that will encourage people in our community to consider 'partnering' with us to help fund this massive project.
The 'Word' doc attached has some initial wording ideas, however someone with a gift for this type of advertising may well come up with better wording. We're happy for you to use a bit of creativity here.

Target Market(s)

Local businesses, parents and extended families

Industry/Entity Type

School

Requirements
Must have
• Picture of the proposed library.
• Pictures of students from our school.
• You can find information and photos on our school website. http://www.plrgs.example.edu.au/
Should not have
• Anything inappropriate for a Christian School.
• Pictures of random people that aren't from our school - ie, aren't in our school uniform.

```html
<!DOCTYPE html>
<html lang="en">
<head>
<meta charset="utf-8">
<title>Children of Today, Leaders of Tomorrow – Library Fundraising Brochure</title>
<link rel="stylesheet" href="https://fonts.googleapis.com/css2?family=Montserrat:wght@300;400;600;700;800&display=swap">
<style>
:root{
  --bg:#e6e6e6;
  --paper:#ffffff;
  --navy:#1c2747;
  --slate:#3e5877;
  --teal:#4f93ad;
  --cyan:#39afd9;
  --cyan-deep:#2b93bf;
  --yellow:#f6c412;
  --green:#3ba935;
  --ink:#2a2a2a;
  --box:#2f3438;
  --white:#ffffff;
}
*{margin:0;padding:0;box-sizing:border-box}
html,body{width:1200px;height:1000px;overflow:hidden}
body{background:var(--bg);font-family:"Montserrat",sans-serif;position:relative;color:var(--ink)}
.page{position:absolute;width:310px;height:438px;overflow:hidden;box-shadow:0 2px 10px rgba(0,0,0,.12)}

/* Front cover */
.front-cover{left:275px;top:40px;background:var(--paper)}
.library-photo{position:absolute;left:10px;top:10px;right:10px;height:290px;
  background:linear-gradient(135deg,var(--slate) 0%,var(--navy) 45%,#5a4a3e 75%,#d9dde2 100%)}
.invest-panel{position:absolute;left:10px;top:10px;width:128px;height:205px;background:rgba(79,147,173,.6);
  display:flex;flex-direction:column;justify-content:flex-end;padding:0 10px 22px;color:var(--white)}
.invest-panel .small{font-weight:300;font-size:11px;letter-spacing:.5px}
.invest-panel .big{font-weight:800;font-size:19px;line-height:1}
.slogan{position:absolute;left:14px;bottom:16px;text-transform:uppercase;line-height:.98;font-size:22px;letter-spacing:-.5px}
.slogan .bold{font-weight:800}
.slogan .light{font-weight:300}
.slogan .green{color:var(--green)}
.slogan .yellow{color:var(--yellow)}
.school-name{position:absolute;right:14px;top:312px;width:88px;display:flex;align-items:flex-start;gap:5px;
  font-weight:700;font-size:10px;line-height:1.15;color:var(--navy)}
.school-name .dot{flex:none;width:10px;height:10px;border-radius:50%;background:var(--navy);margin-top:1px}

/* Back cover */
.back-cover{left:615px;top:40px}
.lab-photo{position:absolute;inset:0;background:linear-gradient(160deg,#e9d8b4 0%,#c9a77a 35%,#d8c9a8 60%,#8fa9a2 100%)}
.about-panel{position:absolute;left:34px;top:60px;width:250px;height:318px;background:rgba(57,175,217,.72);padding:18px 16px;color:var(--white)}
.about-panel .name{display:flex;align-items:center;gap:6px;font-weight:700;font-size:11px;color:var(--white);margin-bottom:12px}
.about-panel .name .dot{width:14px;height:14px;border-radius:50%;background:var(--white)}
.about-panel p{font-size:9.3px;line-height:1.55;text-transform:uppercase;font-weight:400}

/* Inside spread */
.spread{left:290px;top:520px;width:620px;background:var(--cyan)}
.students-photo{position:absolute;inset:0;background:radial-gradient(ellipse at 70% 60%,rgba(30,80,110,.35),rgba(57,175,217,0) 60%),radial-gradient(ellipse at 20% 80%,rgba(30,80,110,.25),rgba(57,175,217,0) 50%)}
.fold{position:absolute;left:310px;top:0;bottom:0;width:1px;background:rgba(255,255,255,.35)}
.inner{position:absolute;top:0;width:310px;height:100%;color:var(--white)}
.inner-left{left:0;padding:16px 18px}
.inner-right{left:310px;padding:16px 18px}

.partners{display:flex;align-items:center;gap:8px}
.partners .count{width:46px;height:46px;border-radius:50%;background:var(--yellow);color:var(--white);font-weight:800;font-size:15px;display:flex;align-items:center;justify-content:center}
.partners h2{font-weight:800;font-size:17px;line-height:1;color:var(--yellow);text-transform:uppercase}
.rule-label{display:flex;align-items:center;gap:8px;font-size:8px;letter-spacing:1px;text-transform:uppercase;margin:12px 0 6px}
.rule-label::before,.rule-label::after{content:"";flex:1;height:1px;background:rgba(255,255,255,.7)}
.target{display:flex;align-items:center;gap:8px}
.target .amount{font-weight:800;font-size:28px;line-height:.95;color:var(--yellow)}
.target .dollar{width:48px;height:48px;background:var(--yellow);color:var(--navy);font-weight:800;font-size:36px;display:flex;align-items:center;justify-content:center}
.via{font-weight:700;font-size:10px;margin-top:6px;text-transform:uppercase}
.towards{font-size:7px;line-height:1.4;margin-top:4px;text-transform:uppercase}
.towards em{font-style:normal;color:var(--yellow);font-weight:700}
.audience{display:grid;grid-template-columns:1fr 1fr;gap:8px 10px;margin-top:16px;font-size:9px;text-transform:uppercase;line-height:1.2}
.audience .please{font-weight:700;color:var(--white)}
.audience .wide{grid-column:1/3}

.chart{display:flex;align-items:flex-end;gap:4px;height:120px;margin-top:4px}
.bar{flex:1;background:var(--yellow);color:var(--ink);font-weight:700;font-size:7.5px;text-align:center;padding-top:3px}
.ways{margin-top:10px;display:flex;flex-direction:column;gap:5px}
.way{background:var(--box);color:var(--white);font-size:7.5px;font-weight:600;text-transform:uppercase;padding:4px 6px;line-height:1.3}
.where{position:absolute;right:18px;top:182px;font-weight:800;font-size:22px;color:var(--yellow)}
.progress{margin-top:14px;font-size:6.8px;line-height:1.45;text-transform:uppercase}
</style>
</head>
<body>

<section class="page front-cover" aria-label="Front cover">
  <div class="library-photo" role="img" aria-label="Photo of the proposed library with curved bookshelves"></div>
  <div class="invest-panel">
    <span class="small">INVESTING IN</span>
    <span class="big">TOMORROW</span>
  </div>
  <div class="school-name"><span class="dot"></span><span>Pine Lake Ridge G.S.</span></div>
  <h1 class="slogan">
    <span class="bold green">Children</span><br>
    <span class="light green">of today</span><br>
    <span class="bold yellow">Leaders</span><br>
    <span class="light yellow">of tomorrow</span>
  </h1>
</section>

<section class="page back-cover" aria-label="Back cover">
  <div class="lab-photo" role="img" aria-label="Photo of students in school uniform doing a science experiment with test tubes"></div>
  <div class="about-panel">
    <div class="name"><span class="dot"></span>Pine Lake Ridge</div>
    <p>Pine Lake Ridge Grammar School provides quality education in a caring, family based community. We are a school with a different focus, centred on faith and on each child. Our teachers are committed to every student, helping them grow in knowledge, character and service. We believe in partnering with families and encouraging others. What our school has to offer you and your family is worth a visit. Please contact the school office and arrange a tour to see our school in action.</p>
  </div>
</section>

<section class="page spread" aria-label="Inside spread">
  <div class="students-photo" role="img" aria-label="Faint photo of students in school uniform working together"></div>
  <div class="fold"></div>

  <div class="inner inner-left">
    <div class="partners">
      <div class="count">100</div>
      <h2>Partner<br>Sought</h2>
    </div>
    <div class="rule-label">To raise</div>
    <div class="target">
      <div class="amount">$50,000<br>OR MORE</div>
      <div class="dollar">$</div>
    </div>
    <div class="via">By tax deductable donations</div>
    <div class="towards">Towards the cost of constructing <em>our new library, admin and 2 additional classrooms</em> to the PLRGS building fund</div>
    <div class="audience">
      <span>School families</span><span class="please">Please…</span>
      <span>Grandparents</span><span>Church members</span>
      <span></span><span>Christian community</span>
      <span class="wide">Pine Lake Ridge businesses and others…</span>
    </div>
  </div>

  <div class="inner inner-right">
    <div class="rule-label">Donate to the community</div>
    <div class="chart">
      <div class="bar" style="height:20%">$100</div>
      <div class="bar" style="height:30%">$200</div>
      <div class="bar" style="height:42%">$500</div>
      <div class="bar" style="height:56%">$1000</div>
      <div class="bar" style="height:78%">$2000</div>
      <div class="bar" style="height:100%">$5000</div>
    </div>
    <div class="where">WHERE</div>
    <div class="ways" style="width:180px">
      <div class="way">Through the school office directly</div>
      <div class="way">By cheque to: PLRGS, PO Box 482, Pine Lake Ridge, NSW, 2999</div>
      <div class="way">Direct deposit A/C</div>
    </div>
    <p class="progress">Number of partners and progress on money raised will be included in the ‘Communicator’ each week during second term. Individual names will be kept confidential. Business names will be listed in the end of term Communicator and on the school web site.</p>
  </div>
</section>

</body>
</html>
```